-Photo booth rental Web Design Project

Our business is a small photo booth rental service serving the capital region and surrounding areas. The photo booth is a portable booth that fits up to 10 guest. I am looking for a website that will have social media capabilities and also private log ins for clients to view their photo albums online after their event. We provide full service photo booth rentals for all types of parties. I am looking for something fun and unique but also professional and I am also looking to maybe somehow incorporate the age of the photo booth which was invented in 1888. I do not have the photos of our photo booth available because we are just starting up and I wanted to get everything together first but I will provide stock photo booth pictures .Thank you for your patience i know it wont be an easy task with out those things. I added a word document describing information i will need on our website, i am looking for a home page, contact us and book an event page, online gallery page, and pricing. If you need any more information please feel free to contact me. Thanks for your help and I look forward to working with you.

Target Market(s)

For everyone from brides to be for their weddings or private parties, corporate parties, school dances, charity events, community events ect

Industry/Entity Type

Business

Requirements
Nice to have
• social media sharing

```html
<!DOCTYPE html>
<html lang="en">
<head>
<meta charset="utf-8">
<title>Giggle Frame Photo Booth</title>
<link href="https://fonts.googleapis.com/css2?family=Questrial&display=swap" rel="stylesheet">
<style>
:root{
  --tan:#9c8068;
  --espresso:#3e2418;
  --footer-top:#6e4532;
  --footer-bottom:#573323;
  --ink:#3a3a3a;
  --body:#555;
  --header-bg:#fbefea;
  --band:#f1f1f1;
  --card:#f5f5f5;
  --rule:#e2e2e2;
  --booth-black:#1c1a19;
  --curtain:#b3221c;
}
*{margin:0;padding:0;box-sizing:border-box}
html,body{width:761px;height:1200px;overflow:hidden}
body{font-family:"Questrial",sans-serif;color:var(--ink);background:#fff;position:relative}
.abs{position:absolute}

.site-header{left:0;top:0;width:761px;height:68px;background:linear-gradient(#fff6f2,var(--header-bg))}
.brand{left:47px;top:14px;font-size:19px;line-height:19px;color:#3b2a22;display:flex;align-items:center;gap:7px}
.brand .mark{width:13px;height:13px;background:#3b2a22;border-radius:50%}
.nav{left:376px;top:33px;display:flex;gap:27px;font-size:9.5px;color:#333}
.login{left:646px;top:29px;width:68px;height:21px;background:var(--tan);color:#fff;font-size:8.5px;display:flex;align-items:center;justify-content:center}

.hero{left:0;top:68px;width:761px;height:260px;
  background:linear-gradient(90deg,#ede6df 0%,#c99f82 6%,#f6f3ef 11%,#3a2c24 17%,#f4f1ed 23%,#c8957a 30%,#2a211d 35%,#f3eee9 41%,#c69478 48%,#f4f0ec 54%,#2f3347 62%,#f4f1ee 67%,var(--booth-black) 68.5%,var(--booth-black) 71%,var(--curtain) 73%,#8e1712 79%,var(--booth-black) 81%,#5a5552 85%,var(--booth-black) 91%,#fff 92.5%,#fff 100%)}
.dots{left:358px;top:300px;display:flex;gap:3px}
.dots span{width:10px;height:10px;border-radius:50%;background:#222}
.hero-rule{left:0;top:328px;width:761px;height:4px;background:var(--tan)}

h2{font-weight:400;font-size:16.5px;color:#333}
p.copy{font-size:7.6px;line-height:13.5px;color:var(--body)}
.btn{width:81px;height:28px;background:var(--tan);color:#fff;font-size:9.5px;display:flex;align-items:center;justify-content:center}

.welcome-img{left:86px;top:339px;width:132px;height:186px;
  background:linear-gradient(90deg,#5e3624 0%,#9a5c3c 12%,#b98a6a 20%,#8d5236 32%,#3b1e14 40%,#b3221c 46%,#8e1712 58%,#f3efe9 64%,#8d5236 72%,#b98a6a 84%,#5e3624 100%)}
.welcome h2{left:275px;top:359px}
.welcome .copy{left:275px;top:380px;width:437px}
.welcome .btn{left:275px;top:494px}

.feature{left:0;top:550px;width:761px;height:250px;background:var(--band)}
.feature h2{left:47px;top:25px}
.feature .copy{left:47px;width:440px}
.feature .btn{left:47px;top:191px}
.feature-img{left:506px;top:12px;width:182px;height:230px;
  background:linear-gradient(90deg,var(--booth-black) 0%,#262222 12%,#ece3cf 18%,#e6dcc4 26%,var(--curtain) 34%,#1a1a1a 50%,var(--curtain) 62%,var(--booth-black) 74%,#222 92%,#2c5aa0 96%,var(--booth-black) 100%)}

.pricing h2{left:47px;top:817px}
.pricing-img{left:55px;top:844px;width:113px;height:142px;
  background:linear-gradient(90deg,#3a2a22 0%,#3a2a22 8%,#d7d1c8 14%,#eeeae4 34%,var(--curtain) 44%,#8e1712 62%,#2a1e18 70%,#3a2a22 100%)}
.pricing .copy{left:47px;top:995px;width:150px;line-height:12px}
.addons{left:47px;top:1042px;font-size:8.5px;color:#222}
.addons i{display:block;font-size:6.5px;color:#666;line-height:11.5px}
.addons b{font-weight:400;font-size:6.8px;color:#222}

.card{top:821px;width:155px;height:279px;background:var(--card);border:1px solid var(--rule)}
.card-head{height:76px;background:var(--tan);color:#fff;text-align:center;padding-top:10px}
.card.featured .card-head{background:var(--espresso)}
.card-head .tier{font-size:12px;letter-spacing:.3px}
.card-head .price{font-size:28px;line-height:32px}
.card-head .price sup{font-size:14px;vertical-align:10px}
.card-head .note{font-size:7.3px}
.features{list-style:none;padding:4px 14px 0}
.features li{font-size:7.3px;color:#333;text-align:center;border-bottom:1px solid var(--rule);padding:5px 0;line-height:11px;display:flex;justify-content:center;gap:6px}
.features li:last-child{border-bottom:0}
.features svg{flex:none;margin-top:2px}
.more{position:absolute;left:37px;bottom:-7px;width:81px;height:22px;background:var(--espresso);color:#fff;font-size:7.5px;display:flex;align-items:center;justify-content:center}
.card.featured .more{background:var(--tan)}

.site-footer{left:0;top:1128px;width:761px;height:72px;background:linear-gradient(var(--footer-top),var(--footer-bottom))}
.footer-brand{left:47px;top:17px;font-size:12px;color:#fff;display:flex;align-items:center;gap:4px}
.footer-brand .mark{width:8px;height:8px;background:#fff;border-radius:50%}
.copyright{left:47px;top:47px;font-size:7px;color:#e8dcd4}
.social{left:639px;top:30px;display:flex;gap:10px}
.social span{width:19px;height:19px;border-radius:50%}
</style>
</head>
<body>
<header class="site-header abs">
  <div class="brand abs">Giggle Frame<br>photo booth <span class="mark"></span></div>
  <nav class="nav abs"><span>Home</span><span>Pricing</span><span>Book an Event</span><span>Contact Us</span></nav>
  <div class="login abs">Client Log In</div>
</header>

<div class="hero abs" role="img" aria-label="Five friends holding moustache and glasses props beside a black photo booth with red curtain"></div>
<div class="dots abs"><span></span><span></span><span></span><span></span></div>
<div class="hero-rule abs"></div>

<section class="welcome">
  <div class="welcome-img abs" role="img" aria-label="Vintage wooden photo booth with red curtain and checkered floor"></div>
  <h2 class="abs">Welcome to Our Site</h2>
  <p class="copy abs">Aliquam molestie, mi et imperdiet euismod, dui purus auctor tellus, et interdum lacus lectus et ante. Sed accumsan sollicitudin sapien, sit amet adipiscing turpis gravida ac. In congue, neque ac lobortis volutpat, libero mauris varius mi, vitae suscipit ipsum ligula vitae risus. Duis aliquam nibh a dui iaculis viverra id a velit. Vivamus egestas risus in magna varius commodo. Sed semper viverra egestas. Etiam pretium porttitor lectus, vel ornare neque porta volutpat.<br>Aenean a nibh eget turpis vehicula tempus ac sed massa. Vestibulum dolor nulla, ultrices ac tincidunt sed, laoreet non est. Suspendisse lobortis turpis in odio blandit ac interdum lorem euismod. Etiam risus massa, vulputate eu pellentesque et, consectetur a neque.</p>
  <div class="btn abs">Read More</div>
</section>

<section class="feature abs">
  <h2 class="abs">Feature of Photo Booth</h2>
  <p class="copy abs" style="top:55px;line-height:12px">Our Booths feature the latest equipment and technology with SnapTouch screens, social and email uploading, music player ready speaker systems, and dual "Photo Booth" or "Video Booth" modes with 1080p HD</p>
  <p class="copy abs" style="top:83px">Fun entertainment &amp; favors for all event types, ex: weddings, birthday parties, graduations, holiday parties, corporate parties, bar/ bat mitzvahs, bridal showers, baby showers, anniversaries, grand openings, school events, proms, corporate events, promotional events, trade shows, conventions, community &amp; charity events.</p>
  <p class="copy abs" style="top:131px">Aenean a nibh eget turpis vehicula tempus ac sed massa. Vestibulum dolor nulla, ultrices ac tincidunt sed, laoreet non est. Suspendisse lobortis turpis in odio blandit ac interdum lorem euismod. Etiam risus massa, vulputate eu pellentesque et, consectetur a neque.</p>
  <div class="btn abs">Read More</div>
  <div class="feature-img abs" role="img" aria-label="Couple dancing in front of a black and red enclosed photo booth with a touch screen"></div>
</section>

<section class="pricing">
  <h2 class="abs">Our Pricing</h2>
  <div class="pricing-img abs" role="img" aria-label="Dark booth with red curtain, stool and checkered floor"></div>
  <p class="copy abs">Aenean a nibh eget turpis vehicula tempus ac sed massa. Vestibulum dolor nulla, ultrices ac tincidunt sed..</p>
  <div class="addons abs">Add on's:<i style="margin-top:4px">Magnet photo strip frames,</i><i>stand up acrylicphoto strip frames,</i><b>ONLY $100 deposit</b></div>

  <div class="card abs" style="left:217px">
    <div class="card-head"><div class="tier">STANDARD</div><div class="price"><sup>$</sup>675</div><div class="note">Includes: 3 Hours of Service</div></div>
    <ul class="features">
      <li><svg width="7" height="6"><path d="M0.5 3l2 2L6.5 0.5" fill="none" stroke="#333" stroke-width="1.3"/></svg>Set up &amp; Removal</li>
      <li><svg width="7" height="6"><path d="M0.5 3l2 2L6.5 0.5" fill="none" stroke="#333" stroke-width="1.3"/></svg>Professional &amp; friendly<br>booth attendant</li>
      <li><svg width="7" height="6"><path d="M0.5 3l2 2L6.5 0.5" fill="none" stroke="#333" stroke-width="1.3"/></svg>Dvd or usb flash drive<br>of picture</li>
      <li><svg width="7" height="6"><path d="M0.5 3l2 2L6.5 0.5" fill="none" stroke="#333" stroke-width="1.3"/></svg>Guestbook</li>
      <li><svg width="7" height="6"><path d="M0.5 3l2 2L6.5 0.5" fill="none" stroke="#333" stroke-width="1.3"/></svg>Unlimited Prints</li>
      <li><svg width="7" height="6"><path d="M0.5 3l2 2L6.5 0.5" fill="none" stroke="#333" stroke-width="1.3"/></svg>Online Gallery</li>
      <li><svg width="7" height="6"><path d="M0.5 3l2 2L6.5 0.5" fill="none" stroke="#333" stroke-width="1.3"/></svg>Digital Backdrop</li>
    </ul>
    <div class="more">MORE DETAILS</div>
  </div>

  <div class="card featured abs" style="left:389px">
    <div class="card-head"><div class="tier">ULTIMATE</div><div class="price"><sup>$</sup>675</div><div class="note">Includes: 4 Hours of Service</div></div>
    <ul class="features">
      <li><svg width="7" height="6"><path d="M0.5 3l2 2L6.5 0.5" fill="none" stroke="#333" stroke-width="1.3"/></svg>Set up &amp; Removal</li>
      <li><svg width="7" height="6"><path d="M0.5 3l2 2L6.5 0.5" fill="none" stroke="#333" stroke-width="1.3"/></svg>Professional &amp; friendly<br>booth attendant</li>
      <li><svg width="7" height="6"><path d="M0.5 3l2 2L6.5 0.5" fill="none" stroke="#333" stroke-width="1.3"/></svg>Dvd or usb flash drive<br>of picture</li>
      <li><svg width="7" height="6"><path d="M0.5 3l2 2L6.5 0.5" fill="none" stroke="#333" stroke-width="1.3"/></svg>Guestbook</li>
      <li><svg width="7" height="6"><path d="M0.5 3l2 2L6.5 0.5" fill="none" stroke="#333" stroke-width="1.3"/></svg>Unlimited Prints</li>
      <li><svg width="7" height="6"><path d="M0.5 3l2 2L6.5 0.5" fill="none" stroke="#333" stroke-width="1.3"/></svg>Online Gallery</li>
      <li><svg width="7" height="6"><path d="M0.5 3l2 2L6.5 0.5" fill="none" stroke="#333" stroke-width="1.3"/></svg>Digital Backdrop</li>
    </ul>
    <div class="more">MORE DETAILS</div>
  </div>

  <div class="card abs" style="left:560px">
    <div class="card-head"><div class="tier">EXTREME</div><div class="price"><sup>$</sup>675</div><div class="note">Includes: 5 Hours of Service</div></div>
    <ul class="features">
      <li><svg width="7" height="6"><path d="M0.5 3l2 2L6.5 0.5" fill="none" stroke="#333" stroke-width="1.3"/></svg>Set up &amp; Removal</li>
      <li><svg width="7" height="6"><path d="M0.5 3l2 2L6.5 0.5" fill="none" stroke="#333" stroke-width="1.3"/></svg>Professional &amp; friendly<br>booth attendant</li>
      <li><svg width="7" height="6"><path d="M0.5 3l2 2L6.5 0.5" fill="none" stroke="#333" stroke-width="1.3"/></svg>Dvd or usb flash drive<br>of picture</li>
      <li><svg width="7" height="6"><path d="M0.5 3l2 2L6.5 0.5" fill="none" stroke="#333" stroke-width="1.3"/></svg>Guestbook</li>
      <li><svg width="7" height="6"><path d="M0.5 3l2 2L6.5 0.5" fill="none" stroke="#333" stroke-width="1.3"/></svg>Unlimited Prints</li>
      <li><svg width="7" height="6"><path d="M0.5 3l2 2L6.5 0.5" fill="none" stroke="#333" stroke-width="1.3"/></svg>Online Gallery</li>
      <li><svg width="7" height="6"><path d="M0.5 3l2 2L6.5 0.5" fill="none" stroke="#333" stroke-width="1.3"/></svg>Digital Backdrop</li>
    </ul>
    <div class="more">MORE DETAILS</div>
  </div>
</section>

<footer class="site-footer abs">
  <div class="footer-brand abs">Giggle Frame photo booth <span class="mark"></span></div>
  <div class="copyright abs">Copyright © 2014. All Right Reserved</div>
  <div class="social abs" aria-label="Social links">
    <span style="background:#3b5998"></span><span style="background:#4bb6d6"></span><span style="background:#c8232c"></span>
  </div>
</footer>
</body>
</html>
```